Brightmere Pictures Business Card

Hello,

i would like to have a dynamic, creative but tasteful card, colour used, front and back. I have attached a sample card that I liked very much from another individual to give you an idea of the theme/approach, but not colour. Ideally the graphic elements of the Brightmere Logo are brought into the design.

Target Market(s)

North America

Industry/Entity Type

Film Production

Contact Information for Business Card

Nadia Pellwick
President/Founder
Brightmere Pictures Inc.
403 555 2917
nadia@brightmerepictures.tv

Font styles to use
Sans Serif

Colors
6b449b
5c5c5c
fdfdfd
000000

Requirements
Must have
• Logo, name, Company name, email and cell number. no Address line to be included.
Should not have
• any unrelated GFX elements, serif fonts

```html
<!DOCTYPE html>
<html lang="en">
<head>
<meta charset="utf-8">
<title>Brightmere Pictures Business Card</title>
<link href="https://fonts.googleapis.com/css2?family=Lato:wght@400;700;900&display=swap" rel="stylesheet">
<style>
  :root {
    --brand-purple: #6b449b;
    --ink-grey: #5c5c5c;
    --paper: #fdfdfd;
    --ink: #000000;
    --backdrop: #eee9e6;
  }
  * { margin: 0; padding: 0; box-sizing: border-box; }
  html, body {
    width: 1200px;
    height: 994px;
    overflow: hidden;
    background: var(--backdrop);
    font-family: "Lato", sans-serif;
  }
  .canvas { position: relative; width: 1200px; height: 994px; }

  .card {
    position: absolute;
    width: 630px;
    height: 360px;
    box-shadow: 0 10px 24px rgba(0,0,0,0.14);
  }

  /* Front */
  .card-front {
    left: 70px;
    top: 80px;
    background: var(--brand-purple);
  }
  .front-wordmark {
    position: absolute;
    left: 0;
    right: 0;
    top: 50%;
    transform: translateY(-50%);
    text-align: center;
    color: var(--paper);
    font-weight: 900;
    font-size: 62px;
    letter-spacing: -1px;
    line-height: 1;
  }
  .front-tagline {
    display: block;
    margin-top: 10px;
    font-size: 15px;
    font-weight: 900;
    letter-spacing: 14px;
    color: var(--paper);
  }

  /* Back */
  .card-back {
    left: 500px;
    top: 560px;
    background: var(--paper);
  }
  .back-wordmark {
    position: absolute;
    left: 30px;
    top: 0;
    width: 110px;
    height: 360px;
    display: flex;
    align-items: center;
    justify-content: center;
  }
  .back-wordmark span {
    transform: rotate(-90deg);
    white-space: nowrap;
    color: var(--brand-purple);
    font-weight: 900;
    font-size: 52px;
    letter-spacing: -1px;
  }
  .divider-vertical {
    position: absolute;
    left: 170px;
    top: 40px;
    width: 2px;
    height: 280px;
    background: var(--ink);
  }
  .identity {
    position: absolute;
    left: 222px;
    top: 70px;
  }
  .person-name {
    font-size: 34px;
    font-weight: 400;
    color: var(--ink);
    line-height: 1.1;
  }
  .person-title {
    font-size: 21px;
    color: var(--ink);
    margin-top: 2px;
  }
  .company-name {
    font-size: 17px;
    color: var(--brand-purple);
    margin-top: 10px;
  }
  .divider-horizontal {
    position: absolute;
    left: 222px;
    top: 198px;
    width: 330px;
    height: 2px;
    background: var(--ink);
  }
  .contacts {
    position: absolute;
    left: 222px;
    top: 222px;
    list-style: none;
  }
  .contact-row {
    display: flex;
    align-items: center;
    gap: 10px;
    font-size: 22px;
    color: var(--ink);
    height: 36px;
  }
  .contact-row svg { width: 26px; height: 26px; flex: none; }
  .contact-sep { margin-right: 4px; }
</style>
</head>
<body>
<main class="canvas">

  <section class="card card-front" aria-label="Card front">
    <div class="front-wordmark">
      Brightmere
      <span class="front-tagline">PICTURES</span>
    </div>
  </section>

  <section class="card card-back" aria-label="Card back">
    <div class="back-wordmark"><span>Brightmere</span></div>
    <div class="divider-vertical"></div>

    <div class="identity">
      <h1 class="person-name">Nadia Pellwick</h1>
      <p class="person-title">Founder</p>
      <p class="company-name">Brightmere Pictures Inc</p>
    </div>
    <div class="divider-horizontal"></div>

    <ul class="contacts">
      <li class="contact-row">
        <svg viewBox="0 0 26 26" aria-hidden="true">
          <circle cx="13" cy="13" r="11.5" fill="none" stroke="#000" stroke-width="1.6"/>
          <path d="M9 7.5c-1 .8-1.6 2-1 3.6 1 2.8 3.3 5.4 6.3 7 1.4.7 2.6.3 3.5-.7l-2.2-2.1-1.5.9c-1.5-.8-2.8-2.2-3.6-3.8l1-1.4z" fill="#000"/>
        </svg>
        <span class="contact-sep">:</span>
        <span>403 555 2917</span>
      </li>
      <li class="contact-row">
        <svg viewBox="0 0 26 26" aria-hidden="true">
          <rect x="2" y="6" width="22" height="14" fill="#000"/>
          <path d="M2 6l11 8 11-8" fill="none" stroke="#fdfdfd" stroke-width="1.5"/>
        </svg>
        <span class="contact-sep">:</span>
        <span>nadia@brightmerepictures.tv</span>
      </li>
    </ul>
  </section>

</main>
</body>
</html>
```